Etiketten-Design für Frizzanteweine
Zielgruppe
Wir sind ein Weingut und suchen für unsere 3 Frizzanteweine ein neues elegantes, modernes Design.
Aufgabenstellung
Vorlage ist im Anhang zu finden.
Das Grundetikett ist weiß. Die Schriftart Frizzante wird mit Gold gedruckt.
Die 3 Etiketten sollen gleich sein und sich nur in der Hintergrundfarbe unterscheiden.
-> Watercolorhintergrund (Teile davon sollen beim Druck veredelt werden)
Auf den Flaschen sollte stehen:
1.Flasche: Frizzante trocken & Rosskamp mit Logo
HAUPTFARBE GRÜN
2.Flasche: Frizzante halbtrocken & Rosskamp mit Logo
HAUPTFARBE BLAU
3.Flasche: Frizzante Rosé & Rosskamp mit Logo
HAUPTFARBE ROSÈ
Etikettengröße: 9cm breit & 9cm hoch
Im Anhang findet man die Form der Flasche die wir verwenden.

```html
<!DOCTYPE html>
<html lang="de">
<head>
<meta charset="utf-8">
<title>Rosskamp Frizzante Etiketten</title>
<link href="https://fonts.googleapis.com/css2?family=Arimo:wght@400&display=swap" rel="stylesheet">
<style>
  :root {
    --page: #ffffff;
    --white: #ffffff;
    --green: #0bd95a;
    --green-deep: #079a45;
    --green-bright: #0ef53a;
    --green-dark: #03a83a;
    --pink: #f27bdc;
    --pink-soft: #f9b6ec;
    --blue: #879cf6;
    --blue-ink: #4d5ee0;
    --accent-a: rgba(31, 211, 196, 0.45);
    --accent-b: rgba(122, 111, 168, 0.45);
  }
  * { margin: 0; padding: 0; box-sizing: border-box; }
  html, body {
    width: 849px; height: 1200px; overflow: hidden;
    background: var(--page);
    font-family: "Arimo", Arial, sans-serif;
  }
  .sheet { position: relative; width: 849px; height: 1200px; }

  .label {
    position: absolute; width: 362px; height: 362px; overflow: hidden;
    background: var(--base);
  }
  .label--glow {
    background:
      radial-gradient(ellipse 95px 75px at 50% 0%, rgba(255,255,255,0.95), rgba(255,255,255,0) 100%),
      var(--base);
  }
  .label--green { --base: var(--green); --variant: var(--green-deep); }
  .label--pink { --base: var(--pink); --variant: var(--pink-soft); }
  .label--blue { --base: var(--blue); --variant: var(--blue-ink); }
  .label--plain { background: linear-gradient(90deg, var(--green-bright), var(--green-dark) 65%); }

  .label--tl { left: 31px; top: 26px; }
  .label--tr { left: 462px; top: 28px; }
  .label--mid { left: 248px; top: 418px; }
  .label--bl { left: 23px; top: 810px; }
  .label--br { left: 463px; top: 812px; }

  .brand-dot {
    position: absolute; left: 137px; top: 32px; width: 88px; height: 88px;
    border-radius: 50%; background: var(--white);
  }
  .brand-name {
    position: absolute; left: 0; right: 0; top: 148px;
    text-align: center; color: var(--white);
    font-size: 58px; line-height: 1; letter-spacing: 1px;
  }
  .brand-tag {
    position: absolute; left: 0; right: 0; top: 245px;
    text-align: center; color: var(--white);
    font-size: 10px; line-height: 1; letter-spacing: 11px; padding-left: 11px;
  }
  .wine-name {
    position: absolute; left: 0; right: 0; top: 292px;
    text-align: center; font-size: 27px; line-height: 1;
    color: rgba(255,255,255,0.55);
    -webkit-text-stroke: 0.6px rgba(90,90,90,0.55);
  }
  .wine-style {
    position: absolute; left: 0; right: 0; top: 323px;
    text-align: center; font-size: 16px; line-height: 1; letter-spacing: 1px;
    color: var(--variant);
  }
  .wine-line {
    position: absolute; left: 0; right: 0; top: 305px;
    text-align: center; font-size: 28px; line-height: 1; color: var(--white);
  }
  .brand-name--plain { top: 158px; }
  .brand-tag--plain { top: 258px; }
  .brand-dot--plain { top: 44px; }

  .accent-area {
    position: absolute;
  }
  .accent-area--bottom {
    left: 0; bottom: 0; width: 95px; height: 85px;
    background: linear-gradient(45deg, var(--accent-b), var(--accent-a) 45%, rgba(31,211,196,0) 100%);
  }
  .accent-area--top {
    right: 0; top: 0; width: 55px; height: 80px;
    background: linear-gradient(225deg, var(--accent-b), var(--accent-a) 45%, rgba(31,211,196,0) 100%);
  }
</style>
</head>
<body>
<main class="sheet">

  <section class="label label--green label--glow label--tl">
    <div class="accent-area accent-area--top" role="img" aria-label="Aquarell-Blätterzweig"></div>
    <div class="accent-area accent-area--bottom" role="img" aria-label="Aquarell-Blätterzweig"></div>
    <div class="brand-dot"></div>
    <div class="brand-name">Rosskamp</div>
    <div class="brand-tag">WEINGUT</div>
    <div class="wine-name">Frizzante</div>
    <div class="wine-style">trocken</div>
  </section>

  <section class="label label--green label--glow label--tr">
    <div class="accent-area accent-area--top" role="img" aria-label="Aquarell-Blätterzweig"></div>
    <div class="accent-area accent-area--bottom" role="img" aria-label="Aquarell-Blätterzweig"></div>
    <div class="brand-dot"></div>
    <div class="brand-name">Rosskamp</div>
    <div class="brand-tag">WEINGUT</div>
    <div class="wine-name">Frizzante</div>
    <div class="wine-style">trocken</div>
  </section>

  <section class="label label--plain label--mid">
    <div class="brand-dot brand-dot--plain"></div>
    <div class="brand-name brand-name--plain">Rosskamp</div>
    <div class="brand-tag brand-tag--plain">WEINGUT</div>
    <div class="wine-line">Frizzante trocken</div>
  </section>

  <section class="label label--pink label--glow label--bl">
    <div class="accent-area accent-area--top" role="img" aria-label="Aquarell-Blätterzweig"></div>
    <div class="accent-area accent-area--bottom" role="img" aria-label="Aquarell-Blätterzweig"></div>
    <div class="brand-dot"></div>
    <div class="brand-name">Rosskamp</div>
    <div class="brand-tag">WEINGUT</div>
    <div class="wine-name">Frizzante</div>
    <div class="wine-style">Rosé</div>
  </section>

  <section class="label label--blue label--glow label--br">
    <div class="accent-area accent-area--top" role="img" aria-label="Aquarell-Blätterzweig"></div>
    <div class="accent-area accent-area--bottom" role="img" aria-label="Aquarell-Blätterzweig"></div>
    <div class="brand-dot"></div>
    <div class="brand-name">Rosskamp</div>
    <div class="brand-tag">WEINGUT</div>
    <div class="wine-name">Frizzante</div>
    <div class="wine-style">halbtrocken</div>
  </section>

</main>
</body>
</html>
```